Simple and Clean business card design

We would like the design to be simple clean and to incorporate our colors.

We are open to your design and talent, we have the dots in our logo as we think of it as data points and we connect data points for people.

We are open to see the great creative and clean design you bring to the table

Contact Information for Business Card

please include: name, position, email, phone and website

Font styles to use
Sans Serif

Requirements
Must have
• my colors incorporated, simplicity
Nice to have
• lots of white space, simplicity
Should not have
• complexicity/ complex art

```html
<!DOCTYPE html>
<html lang="en">
<head>
<meta charset="utf-8">
<title>Tessly business card</title>
<link rel="stylesheet" href="https://fonts.googleapis.com/css2?family=Montserrat:wght@600;700&family=Mulish:wght@400;800&display=swap">
<style>
  :root {
    --backdrop: #9b9b9b;
    --card: #ffffff;
    --ink: #161616;
    --text: #333333;
    --green: #34a853;
    --blue: #5e86c4;
    --yellow: #f9c013;
    --red: #ef5b55;
  }
  * { box-sizing: border-box; margin: 0; padding: 0; }
  html, body { width: 1021px; height: 1200px; overflow: hidden; }
  body { background: var(--backdrop); position: relative; font-family: "Mulish", sans-serif; }

  .card { position: absolute; width: 753px; height: 429px; background: var(--card); left: 134px; }
  .card--front { top: 119px; }
  .card--back { top: 651px; }

  .wordmark {
    position: absolute; left: 0; right: 0; text-align: center;
    font-family: "Montserrat", sans-serif; font-weight: 600; color: var(--ink);
    letter-spacing: 2px; line-height: 1;
  }
  .wordmark .mark-dot { display: inline-block; border-radius: 50%; background: var(--blue); vertical-align: baseline; }
  .card--front .wordmark { top: 176px; font-size: 142px; }
  .card--front .mark-dot { width: 22px; height: 22px; margin-left: 8px; }
  .card--back .wordmark { top: 95px; font-size: 92px; }
  .card--back .mark-dot { width: 14px; height: 14px; margin-left: 5px; }

  .identity { position: absolute; right: 402px; top: 270px; text-align: right; }
  .identity__company { font-weight: 800; font-size: 27px; color: var(--green); line-height: 1; }
  .identity__role { font-size: 17px; color: var(--text); margin-top: 8px; }

  .divider { position: absolute; left: 374px; top: 269px; width: 2px; height: 60px; background: var(--blue); }

  .contacts { position: absolute; left: 402px; top: 262px; list-style: none; }
  .contacts li { display: flex; align-items: center; height: 25px; font-size: 18px; color: var(--text); }
  .contacts svg { width: 14px; height: 14px; margin-right: 7px; fill: var(--green); flex: none; }
</style>
</head>
<body>
  <section class="card card--front">
    <div class="wordmark">Tessly<span class="mark-dot"></span></div>
  </section>

  <section class="card card--back">
    <div class="wordmark">Tessly<span class="mark-dot"></span></div>

    <div class="identity">
      <p class="identity__company">Tessly.Co</p>
      <p class="identity__role">Founder/ CEO</p>
    </div>

    <div class="divider"></div>

    <ul class="contacts">
      <li>
        <svg viewBox="0 0 24 24" aria-hidden="true"><path d="M6.6 10.8a15.1 15.1 0 0 0 6.6 6.6l2.2-2.2a1 1 0 0 1 1-.25 11.4 11.4 0 0 0 3.6.6 1 1 0 0 1 1 1V20a1 1 0 0 1-1 1A17 17 0 0 1 3 4a1 1 0 0 1 1-1h3.5a1 1 0 0 1 1 1c0 1.25.2 2.45.6 3.6a1 1 0 0 1-.25 1z"/></svg>
        555-014-2387
      </li>
      <li>
        <svg viewBox="0 0 24 24" aria-hidden="true"><path d="M2 5h20v14H2zm2 2v.4l8 5.3 8-5.3V7zm0 2.8V17h16V9.8l-8 5.3z"/></svg>
        mara.lind@tessly.co
      </li>
      <li>
        <svg viewBox="0 0 24 24" aria-hidden="true"><path d="M12 2a10 10 0 1 0 0 20 10 10 0 0 0 0-20zm-1 17.9A8 8 0 0 1 4.2 10.6L9 15.4v1a2 2 0 0 0 2 2zm6.9-2.5A2 2 0 0 0 16 16h-1v-3a1 1 0 0 0-1-1H8v-2h2a1 1 0 0 0 1-1V7h2a2 2 0 0 0 2-2v-.4a8 8 0 0 1 2.9 12.8z"/></svg>
        www.Tessly.co
      </li>
    </ul>
  </section>
</body>
</html>
```